Book Cover Design Book About Commercial Real Estate Investing

I need a book cover designed for my upcoming book.
Need cover for paperback and hardcover book.

The Book is about investing in net lease commercial property.

The book title:

The Ground Rent Handbook
Proven Methods For KVR Asset Buyers
By Lou Barrow

Should be minimalist, clean, authoritative, convey money, trust, & growth
I think I like the colors white red and black.
I want a front cover at this time.

Samples I like are included. - the red white and blacks are my favorites

My company is The KVR Circle
you can learn more about Triple Net Properties at my website
www.TheKVRCircle.com

the symbol NNN = Triple net in commercial real estate

Target Market(s)

Affluent male conservative investors

Industry/Entity Type

Real Estate

Requirements
Nice to have
• Sports Motif - - diagrams of sports plays from playbook
• google - Diagrams of sports plays -

```html
<!DOCTYPE html>
<html lang="en">
<head>
<meta charset="utf-8">
<title>The Ground Rent Handbook – Front Cover</title>
<link rel="stylesheet" href="https://fonts.googleapis.com/css2?family=Righteous&family=Audiowide&family=Roboto:wght@400&family=Tinos&display=swap">
<style>
  :root {
    --cover-blue: #1b8dcb;
    --paper-white: #ffffff;
    --title-red: #e62a2c;
    --title-edge: #5c1414;
    --title-glow: #e8eef4;
    --subtitle-blue: #1b8dcb;
    --strip-text: #ffffff;
  }
  html, body {
    margin: 0;
    padding: 0;
    width: 1079px;
    height: 1200px;
    overflow: hidden;
    background: var(--paper-white);
  }
  .cover {
    position: relative;
    width: 1079px;
    height: 1200px;
    overflow: hidden;
    background: var(--paper-white);
  }
  .top-band {
    position: absolute;
    left: 0; top: 0;
    width: 100%;
    height: 634px;
    background: var(--cover-blue);
  }
  .bottom-strip {
    position: absolute;
    left: 0; bottom: 0;
    width: 100%;
    height: 91px;
    background: var(--cover-blue);
  }
  .spine-shade {
    position: absolute;
    left: 0; top: 0;
    width: 158px;
    height: 1109px;
    background: linear-gradient(90deg,
      rgba(200,205,210,0.30) 0%,
      rgba(150,155,160,0.40) 75%,
      rgba(120,125,130,0.55) 100%);
  }
  .title-text {
    font-family: "Righteous", sans-serif;
    color: var(--title-red);
    -webkit-text-stroke: 1.5px var(--title-edge);
    text-shadow: 4px 4px 0 var(--title-glow);
    letter-spacing: 2px;
    margin: 0;
    font-weight: 400;
    white-space: nowrap;
  }
  .cover-title {
    position: absolute;
    left: 158px;
    right: 0;
    top: 190px;
    text-align: center;
    font-size: 84px;
    line-height: 100px;
  }
  .spine-title {
    position: absolute;
    left: 75px;
    top: 1080px;
    transform-origin: 0 0;
    transform: rotate(-90deg) translateY(-50%);
    font-size: 64px;
    line-height: 1;
    text-shadow: 3px 3px 0 var(--title-glow);
  }
  .subtitle {
    position: absolute;
    left: 166px;
    top: 710px;
    margin: 0;
    font-family: "Audiowide", sans-serif;
    font-size: 50px;
    line-height: 64px;
    color: var(--subtitle-blue);
    transform: skewX(-12deg);
    transform-origin: 0 100%;
    font-weight: 400;
  }
  .author {
    position: absolute;
    left: 166px;
    top: 910px;
    margin: 0;
    font-family: "Audiowide", sans-serif;
    font-size: 50px;
    color: var(--subtitle-blue);
    transform: skewX(-12deg);
    transform-origin: 0 100%;
  }
  .edition-year {
    position: absolute;
    left: 18px;
    bottom: 20px;
    font-family: "Tinos", serif;
    font-size: 44px;
    color: var(--strip-text);
    line-height: 1;
  }
  .website {
    position: absolute;
    right: 30px;
    bottom: 34px;
    font-family: "Roboto", sans-serif;
    font-size: 19px;
    color: var(--strip-text);
    line-height: 1;
  }
</style>
</head>
<body>
  <div class="cover">
    <div class="top-band"></div>
    <div class="bottom-strip"></div>
    <div class="spine-shade"></div>

    <h1 class="title-text cover-title">The Ground Rent<br>Handbook</h1>

    <div class="title-text spine-title">The Ground Rent Handbook</div>

    <h2 class="subtitle">Proven Methods For KVR<br>Asset Buyers.</h2>
    <p class="author">By Lou Barrow</p>

    <div class="edition-year">2002</div>
    <div class="website">www.TheKVRCircle.com</div>
  </div>
</body>
</html>
```